Health care technology software systems

We have a solid logo. We have company colors that will need to be used as well. We just need a great business card design. We sell to health plans but want to be modern
Updates

Need extra days to review

Target Market(s)

Health technology sector selling into Health Plans

Industry/Entity Type

Health Care Technology

Contact Information for Business Card

Name, title, address, phone number, email

Requirements
Must have
• Use of Kembrata corporate colors - Uploaded w/ our logos

```html
<!DOCTYPE html>
<html lang="en">
<head>
<meta charset="utf-8">
<title>Kembrata Business Card</title>
<link rel="stylesheet" href="https://fonts.googleapis.com/css2?family=Montserrat:wght@300&family=Open+Sans:wght@400;600&display=swap">
<style>
  :root {
    --brand-blue: #3b5dab;
    --brand-green: #7dc242;
    --brand-sky: #22a7e0;
    --ink-dark: #3a3a3a;
    --ink-mid: #444444;
    --paper: #ffffff;
    --page: #ffffff;
  }
  * { margin: 0; padding: 0; box-sizing: border-box; }
  html, body {
    width: 1200px; height: 1200px; overflow: hidden;
    background: var(--page);
  }
  .stage { position: relative; width: 1200px; height: 1200px; }
  .card {
    position: absolute; left: 192px; width: 814px; height: 466px;
    box-shadow: 8px 9px 10px rgba(0,0,0,0.45);
    overflow: hidden;
  }
  .card-front { top: 108px; background: var(--brand-blue); }
  .card-back { top: 625px; background: var(--brand-blue); }

  .wordmark {
    position: absolute; display: flex; align-items: center;
    font-family: "Montserrat", sans-serif; font-weight: 300;
    white-space: nowrap;
  }
  .wordmark-dot { border-radius: 50%; flex: none; }
  .card-front .wordmark {
    left: 104px; top: 182px; gap: 30px;
    font-size: 104px; color: var(--paper); line-height: 1;
  }
  .card-front .wordmark-dot { width: 112px; height: 112px; background: var(--brand-green); }
  .card-back .wordmark {
    left: 66px; top: 70px; gap: 28px;
    font-size: 76px; color: var(--ink-dark); line-height: 1; z-index: 2;
  }
  .card-back .wordmark-dot { width: 84px; height: 84px; background: var(--brand-sky); }

  .back-art { position: absolute; inset: 0; }

  .holder {
    position: absolute; left: 66px; top: 212px; z-index: 2;
    font-family: "Open Sans", sans-serif; color: var(--ink-mid);
  }
  .holder-name { font-size: 31px; font-weight: 600; line-height: 1.2; }
  .holder-title { font-size: 19px; font-weight: 400; letter-spacing: 0.5px; margin-top: 4px; }

  .contact {
    position: absolute; z-index: 2;
    font-family: "Open Sans", Arial, sans-serif; font-size: 21px;
    color: var(--paper); letter-spacing: 0.6px;
  }
  .contact-row { display: flex; align-items: center; gap: 10px; height: 46px; }
  .contact-list { left: 66px; top: 355px; }
  .contact-address { left: 504px; top: 380px; display: flex; align-items: center; gap: 20px; line-height: 1.35; }
  .icon { fill: var(--brand-green); flex: none; }
</style>
</head>
<body>
<main class="stage">
  <section class="card card-front" aria-label="Card front">
    <div class="wordmark">
      <span class="wordmark-dot"></span>
      <span class="wordmark-name">Kembrata</span>
    </div>
  </section>

  <section class="card card-back" aria-label="Card back">
    <svg class="back-art" width="814" height="466" viewBox="0 0 814 466" aria-hidden="true">
      <path d="M0 0 H796 C735 150 565 288 340 302 C200 311 90 318 0 323 Z" fill="var(--paper)"/>
      <path d="M336 296 C560 252 704 128 760 0 L776 0 C724 136 580 258 336 296 Z" fill="var(--brand-green)"/>
    </svg>

    <div class="wordmark">
      <span class="wordmark-dot"></span>
      <span class="wordmark-name">Kembrata</span>
    </div>

    <div class="holder">
      <p class="holder-name">Your Name:</p>
      <p class="holder-title">Title</p>
    </div>

    <div class="contact contact-list">
      <p class="contact-row">
        <svg class="icon" width="26" height="26" viewBox="0 0 24 24" aria-hidden="true"><path d="M6.6 10.8a15.1 15.1 0 0 0 6.6 6.6l2.2-2.2a1 1 0 0 1 1-.25 11.4 11.4 0 0 0 3.6.57 1 1 0 0 1 1 1V20a1 1 0 0 1-1 1A17 17 0 0 1 3 4a1 1 0 0 1 1-1h3.5a1 1 0 0 1 1 1c0 1.25.2 2.46.57 3.6a1 1 0 0 1-.25 1z"/></svg>
        <span>01+2345 6789 0123</span>
      </p>
      <p class="contact-row">
        <svg class="icon" width="28" height="20" viewBox="0 0 28 20" aria-hidden="true"><path d="M0 0 H28 V20 H0 Z M2 2 L14 11 L26 2" /><path d="M2 3 L14 12 L26 3 V18 L18 10 L14 13 L10 10 L2 18 Z" fill="var(--brand-blue)" opacity="0.35"/></svg>
        <span>info@company.com</span>
      </p>
    </div>

    <div class="contact contact-address">
      <svg class="icon" width="30" height="46" viewBox="0 0 30 46" aria-hidden="true">
        <path d="M15 0 A13 13 0 0 1 28 13 C28 23 15 36 15 36 C15 36 2 23 2 13 A13 13 0 0 1 15 0 Z M15 7 A6 6 0 1 0 15.01 7 Z"/>
        <ellipse cx="15" cy="42" rx="13" ry="3.5"/>
      </svg>
      <p>Street Loation,<br>state,country.</p>
    </div>
  </section>
</main>
</body>
</html>
```